professional business card

A Clean looking business card for a money transfer company. Our company is call Velorix= Transfer + Send = Transcend (next level)
to show professionalism as well as some effects to show digital tech.

1 side to have position, name and address
2 side to have company name and show that we provide money exchange and cross-border money transfer

Target Market(s)

Remittance companies and high net worth individuals

Industry/Entity Type

Finance

Contact Information for Business Card

Name, address, email, title, services- money exchange and cross-border remittance

Requirements
Nice to have
• Digital age feel

```html
<!DOCTYPE html>
<html lang="en">
<head>
<meta charset="UTF-8">
<title>Velorix Business Card</title>
<link href="https://fonts.googleapis.com/css2?family=Open+Sans:wght@400;600&display=swap" rel="stylesheet">
<style>
  :root {
    --navy: #1b2836;
    --navy-deep: #131d28;
    --teal: #5fc3d3;
    --white: #ffffff;
    --paper: #f6f8f9;
    --ink: #2a3542;
    --muted: #a9b6c2;
    --stage: #e6e8ea;
  }
  * { box-sizing: border-box; margin: 0; padding: 0; }
  html, body {
    width: 1200px; height: 1023px; overflow: hidden;
    background: var(--stage);
    font-family: "Open Sans", Arial, sans-serif;
  }
  .canvas {
    width: 1200px; height: 1023px;
    display: flex; flex-direction: column; align-items: center; justify-content: center;
    gap: 60px;
  }
  .card {
    position: relative; width: 700px; height: 400px; overflow: hidden;
    border-radius: 4px;
    box-shadow: 0 6px 18px rgba(0,0,0,0.18);
  }
  /* Front */
  .card-front {
    background: linear-gradient(135deg, #22323f 0%, var(--navy) 50%, var(--navy-deep) 100%);
    display: flex; flex-direction: column; align-items: center; justify-content: center;
    gap: 26px;
  }
  .brand { display: flex; align-items: center; gap: 22px; }
  .brand-dot { width: 58px; height: 58px; border-radius: 50%; background: var(--teal); }
  .brand-name {
    font-weight: 600; font-size: 64px; letter-spacing: 2px;
    color: var(--white); text-transform: uppercase; line-height: 1;
  }
  .services {
    font-size: 14px; letter-spacing: 3px; text-transform: uppercase;
    color: var(--muted); display: flex; align-items: center; gap: 14px;
  }
  .services .sep { width: 5px; height: 5px; border-radius: 50%; background: var(--teal); }
  /* Back */
  .card-back { background: var(--paper); }
  .card-back .brand { position: absolute; left: 50px; top: 48px; gap: 16px; }
  .card-back .brand-dot { width: 40px; height: 40px; }
  .card-back .brand-name { color: var(--ink); font-size: 48px; }
  .holder { position: absolute; left: 50px; top: 140px; }
  .holder-name { font-size: 20px; color: var(--ink); letter-spacing: 1px; text-transform: uppercase; }
  .holder-title { font-size: 15px; color: var(--teal); margin-top: 2px; }
  .contacts { list-style: none; margin-top: 12px; }
  .contacts li {
    display: flex; align-items: center; gap: 10px;
    font-size: 15px; color: var(--ink); line-height: 23px;
  }
  .contacts svg { width: 13px; height: 13px; fill: var(--teal); flex: none; }
  .address {
    position: absolute; right: 50px; top: 230px; text-align: right;
    font-size: 15px; color: var(--ink); line-height: 22px; font-style: normal;
  }
  .sweep { position: absolute; left: 0; bottom: 0; width: 700px; height: 400px; }
</style>
</head>
<body>
<main class="canvas">
  <section class="card card-front" aria-label="Card front">
    <div class="brand">
      <span class="brand-dot"></span>
      <span class="brand-name">Velorix</span>
    </div>
    <p class="services">Money Exchange <span class="sep"></span> Cross-Border Remittance</p>
  </section>

  <section class="card card-back" aria-label="Card back">
    <svg class="sweep" viewBox="0 0 700 400" aria-hidden="true">
      <path d="M0 310 C 200 395, 450 400, 700 360 L700 400 L0 400 Z" fill="var(--teal)"/>
      <path d="M0 322 C 200 405, 450 410, 700 372 L700 400 L0 400 Z" fill="var(--paper)"/>
      <path d="M0 330 C 200 412, 450 418, 700 380 L700 400 L0 400 Z" fill="var(--navy)"/>
    </svg>
    <div class="brand">
      <span class="brand-dot"></span>
      <span class="brand-name">Velorix</span>
    </div>
    <div class="holder">
      <p class="holder-name">Daniel Morrow</p>
      <p class="holder-title">Manager</p>
      <ul class="contacts">
        <li><svg viewBox="0 0 16 16"><path d="M3 1h3l1.5 4-2 1.2a9 9 0 0 0 4.3 4.3L11 8.5l4 1.5v3a2 2 0 0 1-2 2A13 13 0 0 1 1 3a2 2 0 0 1 2-2z"/></svg>555-201-4478</li>
        <li><svg viewBox="0 0 16 16"><rect x="4" y="1" width="8" height="14" rx="1.5"/></svg>555-201-4479</li>
        <li><svg viewBox="0 0 16 16"><path d="M1 3h14v10H1z M1 3l7 6 7-6"/></svg>info@velorixpay.com</li>
        <li><svg viewBox="0 0 16 16"><circle cx="8" cy="8" r="7"/></svg>www.velorixpay.com</li>
      </ul>
    </div>
    <address class="address">
      1420 Harbor View Road<br>
      Juneau, Alaska 99801
    </address>
  </section>
</main>
</body>
</html>
```